Wendale Information Posters for Student signage

Secondary school looking for some posters to display throughout the school with fresh designs using school colours and fitting with general feel of the school's graphic image. The final designs should be welcoming but clearly outline the required instructions. Sample designs that have been created by the school are attached with the relevant information that is required to appear on the signs. School would like a more dynamic design than the basic signs attached.
We are looking for:
- Large pop-up banner style size for the 2 posters called
"Ready for class" and "Morning Routine".
- Printable poster for the "Wendale Outdoor" sign.

Please incorporate a design feature of "the Wendale 1,2,3" into the posters and also use the Wendale Leaner values of Integrity, Compassion, Curiosity and Drive to help illustrate the content.

An option for design is to incorporate our school's first nations artwork into the design and i have also provided various extracts of design pieces that the school often uses in it's marketing materials.

Target Market(s)

Secondary School Students

Industry/Entity Type

Education

Colors
00AB8E
00BBA5
67D7C9
C6EFE9
E9F9F6
FFF300
FFF600
FEFA6F
FFFEC7
FFFEE8
FFC000
F8CF3A
FAE287
FDF2CF
FEFAEE

Requirements
Must have
• My project must have eyecatching graphics

```html
<!DOCTYPE html>
<html lang="en">
<head>
<meta charset="utf-8">
<title>Wendale – Are You Ready for Class</title>
<link rel="stylesheet" href="https://fonts.googleapis.com/css2?family=Archivo+Black&family=Arimo:wght@700&family=Poppins:wght@500;600&family=Crimson+Pro:ital,wght@1,400&display=swap">
<style>
  :root{
    --stage:#646464;
    --forest:#1d3a20;
    --forest-deep:#173319;
    --forest-mid:#2c5a2c;
    --cream:#ede9e1;
    --yellow:#fde50a;
    --yellow-soft:#f5e03a;
    --orange:#f26522;
    --olive:#b9b84a;
    --white:#ffffff;
    --ink:#1f2a20;
  }
  *{box-sizing:border-box;margin:0;padding:0}
  html,body{width:1200px;height:2583px;overflow:hidden;background:var(--stage)}
  .banner{position:absolute;left:116px;top:123px;width:961px;height:2330px;background:var(--cream);overflow:hidden}
  .layer{position:absolute;left:0;top:0;width:961px;height:2330px}
  .title-box{position:absolute;left:149px;top:215px;width:660px;height:287px;background:var(--yellow);border-radius:44px}
  .title-box__name{position:absolute;left:17px;top:17px;width:626px;height:129px;background:var(--white);border-radius:30px 30px 0 0;
    font-family:"Arimo",Arial,sans-serif;font-weight:700;font-size:92px;color:var(--forest);text-align:center;line-height:129px;letter-spacing:-1px}
  .step{position:absolute;top:163px;width:96px;height:96px;border-radius:50%;background:var(--forest);color:var(--white);
    font-family:"Arimo",Arial,sans-serif;font-weight:700;font-size:58px;line-height:96px;text-align:center}
  .headline{position:absolute;left:0;width:961px;text-align:center;font-family:"Archivo Black",sans-serif;color:var(--forest);line-height:1}
  .headline--small{top:582px;font-size:116px}
  .headline--big{top:680px;font-size:204px;letter-spacing:-2px}
  .class-pill{position:absolute;left:93px;top:894px;width:778px;height:115px;border-radius:58px;background:var(--yellow);overflow:hidden;border:2px solid var(--white)}
  .class-pill__for{position:absolute;left:0;top:0;width:232px;height:100%;background:var(--orange);color:var(--white);
    font-family:"Archivo Black",sans-serif;font-size:66px;line-height:111px;text-align:center;border-radius:0 60px 60px 0}
  .class-pill__class{position:absolute;left:260px;top:0;font-family:"Archivo Black",sans-serif;font-size:100px;line-height:111px;color:var(--forest)}
  .kit{position:absolute;top:1082px;width:232px;text-align:center}
  .kit__badge{display:block;width:232px;height:232px}
  .kit__label{margin-top:12px;font-family:"Poppins",sans-serif;font-weight:600;font-size:36px;line-height:44px;color:var(--forest)}
  .kit__note{font-family:"Poppins",sans-serif;font-weight:500;font-size:20px;line-height:28px;color:var(--ink)}
  .values{position:absolute;left:87px;top:1534px;width:788px;height:193px;background:var(--white);border-radius:28px;box-shadow:0 22px 22px -14px rgba(0,0,0,.35)}
  .values__tag{position:absolute;left:194px;top:1512px;width:574px;height:52px;border-radius:26px;background:var(--forest);color:var(--yellow);
    font-family:"Poppins",sans-serif;font-weight:600;font-size:34px;line-height:52px;text-align:center}
  .values__col{position:absolute;top:1595px;list-style:none}
  .values__col li{display:flex;align-items:center;gap:10px;height:50px;font-family:"Poppins",sans-serif;font-weight:600;font-size:35px;color:var(--ink)}
  .values__col svg{width:34px;height:34px;flex:none}
  .values__rule{position:absolute;left:491px;top:1595px;height:100px;border-left:2px dotted #d7cc57}
  .school-name{position:absolute;left:70px;top:1845px;display:flex;align-items:center;gap:18px;
    font-family:"Poppins",sans-serif;font-weight:600;font-size:40px;color:var(--forest)}
  .school-name__dot{width:70px;height:70px;border-radius:50%;background:var(--yellow);border:6px solid var(--forest)}
  .tagline{position:absolute;left:0;top:2240px;width:961px;text-align:center;font-family:"Crimson Pro",serif;font-style:italic;font-size:44px;color:var(--yellow-soft);word-spacing:4px}
  .tagline span{margin:0 18px}
  .tagline .muted{color:#f0ead0}
</style>
</head>
<body>
<main class="banner">
  <!-- Top artwork band -->
  <svg class="layer" viewBox="0 0 961 2330" aria-hidden="false">
    <defs>
      <radialGradient id="artGlow" cx="0.78" cy="0.25" r="0.7">
        <stop offset="0" stop-color="#3e7a3a"/>
        <stop offset="1" stop-color="#173319"/>
      </radialGradient>
      <radialGradient id="artGlowLow" cx="0.85" cy="0.8" r="0.7">
        <stop offset="0" stop-color="#3b7537"/>
        <stop offset="1" stop-color="#173319"/>
      </radialGradient>
    </defs>
    <path role="img" aria-label="First Nations dot artwork in deep greens" fill="url(#artGlow)"
      d="M0 0H961V560C800 500 620 470 420 490C260 505 120 560 0 650Z"/>
    <path d="M0 520C120 470 240 445 360 445" stroke="#fff" stroke-width="6" fill="none"/>
    <path d="M0 560C120 500 240 470 360 468" stroke="#fff" stroke-width="5" stroke-dasharray="2 12" stroke-linecap="round" fill="none"/>
    <path d="M0 600C120 530 240 495 360 492" stroke="#fff" stroke-width="6" fill="none"/>
    <path d="M809 360C870 370 920 385 961 400" stroke="#fff" stroke-width="5" stroke-dasharray="2 12" stroke-linecap="round" fill="none"/>
    <path d="M809 420C870 440 920 460 961 475" stroke="#fff" stroke-width="6" fill="none"/>
    <path d="M760 470C840 485 900 500 961 520" stroke="var(--yellow)" stroke-width="18" fill="none"/>

    <!-- Bottom artwork band -->
    <path role="img" aria-label="First Nations dot artwork in deep greens" fill="url(#artGlowLow)"
      d="M0 2000C240 2030 520 1960 700 1930C820 1910 900 1905 961 1900V2330H0Z"/>
    <path d="M300 2010C520 1960 740 1905 961 1880" stroke="#2e7d32" stroke-width="22" fill="none"/>
    <path d="M300 2040C520 1985 740 1930 961 1912" stroke="var(--yellow)" stroke-width="20" fill="none"/>
    <path d="M330 2075C540 2025 760 1975 961 1960" stroke="#fff" stroke-width="5" stroke-dasharray="2 12" stroke-linecap="round" fill="none"/>
    <path d="M330 2110C540 2055 760 2005 961 1995" stroke="#fff" stroke-width="6" fill="none"/>
    <path d="M330 2150C540 2100 760 2050 961 2040" stroke="#fff" stroke-width="5" stroke-dasharray="2 12" stroke-linecap="round" fill="none"/>
    <path d="M0 2080C60 2090 120 2120 170 2160" stroke="#fff" stroke-width="6" fill="none"/>
    <path d="M0 2120C60 2130 120 2160 170 2200" stroke="#fff" stroke-width="5" stroke-dasharray="2 12" stroke-linecap="round" fill="none"/>
  </svg>

  <section class="title-box">
    <h1 class="title-box__name">The Wendale</h1>
    <span class="step" style="left:107px">1</span>
    <span class="step" style="left:281px">2</span>
    <span class="step" style="left:458px">3</span>
  </section>

  <h2 class="headline headline--small">ARE YOU</h2>
  <h2 class="headline headline--big">READY</h2>
  <div class="class-pill"><span class="class-pill__for">FOR</span><span class="class-pill__class">CLASS</span></div>

  <div class="kit" style="left:78px">
    <svg class="kit__badge" viewBox="0 0 232 232">
      <circle cx="116" cy="116" r="114" fill="var(--olive)"/><circle cx="116" cy="116" r="98" fill="var(--forest)"/>
      <g fill="none" stroke="#fff" stroke-width="4" stroke-linejoin="round">
        <rect x="66" y="62" width="100" height="76" rx="6"/>
        <path d="M50 146H182L174 158H58Z"/>
        <path d="M116 74L138 82V100C138 114 128 122 116 127C104 122 94 114 94 100V82Z"/>
        <path d="M105 100L113 108L128 92"/>
      </g>
    </svg>
    <p class="kit__label">Laptop/<br>workbook</p>
  </div>
  <div class="kit" style="left:373px">
    <svg class="kit__badge" viewBox="0 0 232 232">
      <circle cx="116" cy="116" r="114" fill="var(--olive)"/><circle cx="116" cy="116" r="98" fill="var(--forest)"/>
      <g fill="none" stroke="#fff" stroke-width="4" stroke-linejoin="round" stroke-linecap="round">
        <rect x="84" y="48" width="64" height="120" rx="10"/>
        <path d="M106 58H126"/>
        <path d="M116 118V88C116 82 126 82 126 88V116L146 120C154 122 158 128 156 136L150 166H112L96 140C93 134 100 128 106 132L116 142"/>
      </g>
    </svg>
    <p class="kit__label">Phone<br>in Pouchlok</p>
  </div>
  <div class="kit" style="left:662px">
    <svg class="kit__badge" viewBox="0 0 232 232">
      <circle cx="116" cy="116" r="114" fill="var(--olive)"/><circle cx="116" cy="116" r="98" fill="var(--forest)"/>
      <g fill="none" stroke="#fff" stroke-width="4" stroke-linejoin="round" stroke-linecap="round">
        <path d="M84 48L116 36L148 48L116 60Z"/><path d="M98 54V66C110 72 122 72 134 66V54"/>
        <path d="M148 48V62"/>
        <path d="M74 170V96L100 84L116 104L132 84L158 96V170Z"/>
        <path d="M110 104L116 150L122 104"/>
        <path d="M136 140H158"/>
      </g>
    </svg>
    <p class="kit__label">Correct<br>uniform</p>
    <p class="kit__note">(Including hat)</p>
  </div>

  <section class="values" aria-label="Wendale Leaner values"></section>
  <h3 class="values__tag">★ Wendale Leaner values ★</h3>
  <ul class="values__col" style="left:150px">
    <li><svg viewBox="0 0 34 34"><path d="M17 3L29 8V16C29 24 23 29 17 31C11 29 5 24 5 16V8Z" fill="none" stroke="#2c5a2c" stroke-width="2.5"/><path d="M11 17L15 21L23 13" fill="none" stroke="#2c5a2c" stroke-width="2.5"/></svg>Integrity</li>
    <li><svg viewBox="0 0 34 34"><path d="M17 3L29 8V16C29 24 23 29 17 31C11 29 5 24 5 16V8Z" fill="none" stroke="#2c5a2c" stroke-width="2.5"/><path d="M11 17L15 21L23 13" fill="none" stroke="#2c5a2c" stroke-width="2.5"/></svg>Compassion</li>
  </ul>
  <span class="values__rule"></span>
  <ul class="values__col" style="left:530px">
    <li><svg viewBox="0 0 34 34"><path d="M17 3L29 8V16C29 24 23 29 17 31C11 29 5 24 5 16V8Z" fill="none" stroke="#2c5a2c" stroke-width="2.5"/><path d="M11 17L15 21L23 13" fill="none" stroke="#2c5a2c" stroke-width="2.5"/></svg>Curiosity and</li>
    <li><svg viewBox="0 0 34 34"><path d="M17 3L29 8V16C29 24 23 29 17 31C11 29 5 24 5 16V8Z" fill="none" stroke="#2c5a2c" stroke-width="2.5"/><path d="M11 17L15 21L23 13" fill="none" stroke="#2c5a2c" stroke-width="2.5"/></svg>Drive</li>
  </ul>

  <div class="school-name"><span class="school-name__dot"></span>Wendale State High</div>

  <p class="tagline"><span>Prepared.</span><span class="muted">Focused.</span><span>Ready to Learn</span></p>
</main>
</body>
</html>
```